Need simple and modern looking business card with all my information on one side and logo on the other side
Info :
Company name - VELMAR CONSTRUCTION LLC
Company addres- 418 harbor 87th. Dunmoor park ny 10352
Email- velmarllc@tridomail.Com
Company phone number 555-318-6094
Cell number- 555-742-0583
Web site - velmarllc.Com
My name Gerald tomasino

Target Market(s)

Construction , home improvement, remodeling

Industry/Entity Type

Construction

Contact Information for Business Card

It has to be moder but at the same time simple

Font styles to use
Sans Serif

Colors
0255a3
ffffff
000000
f78f20
b1b1b1
9d9d9d
1b1b1b
33a6d7
ec1f27

Requirements
Must have
• My logo on one side maybe with a some kind of background on the other side all my information
Nice to have
• Some kind of background pictures provided by you .PLEASE HAVE ACCOUNT WITH PIXELVAULT WILL NOT PAY ANY EXTRA FEES .
Should not have
• Any kind of hamer, nails,screws, helmets itp. Please do not copy the other designs come up with something new.

```html
<!DOCTYPE html>
<html lang="en">
<head>
<meta charset="utf-8">
<title>Velmar Construction LLC – Business Card</title>
<link rel="stylesheet" href="https://fonts.googleapis.com/css2?family=Open+Sans:wght@400;600;700&display=swap">
<style>
  :root {
    --blue: #0255a3;
    --white: #ffffff;
    --black: #000000;
    --orange: #f78f20;
    --grey-light: #b1b1b1;
    --grey: #9d9d9d;
    --charcoal: #1b1b1b;
    --sky: #33a6d7;
    --red: #ec1f27;
    --backdrop: #e6e6e6;
    --text: #3a3a3a;
  }
  * { box-sizing: border-box; margin: 0; padding: 0; }
  html, body {
    width: 1200px;
    height: 900px;
    overflow: hidden;
  }
  body {
    background: var(--backdrop);
    font-family: "Open Sans", Arial, sans-serif;
    position: relative;
  }
  .card {
    position: absolute;
    width: 620px;
    height: 354px;
    border-radius: 4px;
    overflow: hidden;
    box-shadow: 0 6px 18px rgba(0,0,0,0.18);
  }

  /* Logo side */
  .card-back {
    left: 520px;
    top: 56px;
    background: linear-gradient(135deg, #333333 0%, #2a2a2a 50%, var(--charcoal) 100%);
  }
  .card-back .wordmark {
    position: absolute;
    right: 40px;
    bottom: 60px;
    color: var(--white);
  }

  .wordmark {
    display: flex;
    align-items: center;
    gap: 12px;
    font-family: "Open Sans", Arial, sans-serif;
    font-weight: 600;
    text-transform: uppercase;
    line-height: 1.05;
  }
  .wordmark-square {
    width: 18px;
    height: 18px;
    background: var(--orange);
    flex: none;
  }
  .wordmark-text {
    display: flex;
    flex-direction: column;
  }
  .wordmark-main { font-size: 44px; letter-spacing: 2px; }
  .wordmark-sub  { font-size: 17px; letter-spacing: 3.2px; }

  /* Info side */
  .card-front {
    left: 80px;
    top: 486px;
    background: var(--white);
  }
  .card-front .decor {
    position: absolute;
    inset: 0;
  }
  .holder-name {
    position: absolute;
    left: 40px;
    top: 40px;
    font-size: 17px;
    font-weight: 700;
    color: var(--orange);
  }
  .holder-name .surname { color: var(--red); }

  .contact-list {
    position: absolute;
    left: 40px;
    top: 112px;
    list-style: none;
    font-size: 14px;
    color: var(--text);
    line-height: 19px;
  }
  .contact-list li {
    display: flex;
    align-items: center;
    gap: 8px;
  }
  .contact-list svg { width: 10px; height: 10px; flex: none; }
  .address {
    position: absolute;
    left: 40px;
    top: 198px;
    font-size: 14px;
    line-height: 18px;
    color: var(--text);
    font-style: normal;
  }
  .card-front .wordmark {
    position: absolute;
    right: 34px;
    top: 132px;
    color: var(--black);
  }
  .card-front .wordmark-main { font-size: 40px; }
  .card-front .wordmark-sub { font-size: 15.5px; }
</style>
</head>
<body>

<section class="card card-back" aria-label="Logo side">
  <div class="wordmark">
    <span class="wordmark-square"></span>
    <span class="wordmark-text">
      <span class="wordmark-main">Velmar</span>
      <span class="wordmark-sub">Construction LLC</span>
    </span>
  </div>
</section>

<section class="card card-front" aria-label="Information side">
  <svg class="decor" viewBox="0 0 620 354" width="620" height="354" aria-hidden="true">
    <polygon points="0,0 22,0 0,22" fill="var(--orange)"/>
    <polygon points="30,0 58,0 36,34 8,34" fill="var(--red)"/>
    <polygon points="0,262 286,262 272,284 0,284" fill="var(--orange)"/>
    <polygon points="288,290 620,290 620,340 256,340" fill="var(--red)"/>
  </svg>

  <h1 class="holder-name">Gerald <span class="surname">tomasino</span></h1>

  <ul class="contact-list">
    <li>
      <svg viewBox="0 0 10 10"><rect x="2.5" y="0.5" width="5" height="9" rx="1" fill="none" stroke="var(--orange)" stroke-width="1.2"/></svg>
      555-742-0583
    </li>
    <li>
      <svg viewBox="0 0 10 10"><path d="M2 0.5 L4 2.5 L3 4 Q4.5 6 6 7 L7.5 6 L9.5 8 L8 9.5 Q3 8.5 0.5 2 Z" fill="var(--orange)"/></svg>
      555-318-6094
    </li>
    <li>
      <svg viewBox="0 0 10 10"><rect x="0.5" y="2" width="9" height="6.5" fill="var(--orange)"/><path d="M0.5 2 L5 5.5 L9.5 2" fill="none" stroke="var(--white)" stroke-width="0.9"/></svg>
      velmarllc@tridomail.Com
    </li>
    <li>
      <svg viewBox="0 0 10 10"><circle cx="5" cy="5" r="4.5" fill="var(--orange)"/><path d="M0.5 5 H9.5 M5 0.5 Q2.5 5 5 9.5 M5 0.5 Q7.5 5 5 9.5" fill="none" stroke="var(--white)" stroke-width="0.7"/></svg>
      www.velmarllc.com
    </li>
  </ul>

  <address class="address">418 harbor 87th. Dunmoor<br>park ny 10352</address>

  <div class="wordmark">
    <span class="wordmark-square"></span>
    <span class="wordmark-text">
      <span class="wordmark-main">Velmar</span>
      <span class="wordmark-sub">Construction LLC</span>
    </span>
  </div>
</section>

</body>
</html>
```